Brackwell Immigration Law

We need a web design for our existing company www.brackwellcounsel.co.uk. We are an immigration consultancy. The final design should communicate professionalism, integrity and affordability.

Industry/Entity Type

It Company

Logo Text

Brackwell Counsel Partners

Number of Pages Required

5+ page

Font styles to use
Serif

Requirements
Must have
• I want to have the same silhouette logo but something different in positioning..
Nice to have
• Please have a look at these websites:
• https://www.travelpathguide.co.uk/visa_uk/
• http://www.oakdenadvisers.co.uk/
• http://www.myrtlegatelaw.org/index.php
• www.brackwellcounsel.co.uk

```html
<!DOCTYPE html>
<html lang="en">
<head>
<meta charset="utf-8">
<title>Brackwell Counsel Partners — Student Visa</title>
<link href="https://fonts.googleapis.com/css2?family=Open+Sans:ital,wght@0,400;0,600;0,700;0,800;1,400&family=Oswald:wght@400;500&display=swap" rel="stylesheet">
<style>
:root{
  --orange:#f26b21;
  --ink:#222;
  --text:#666;
  --muted:#999;
  --line:#e2e2e2;
  --paper:#fff;
  --soft:#f1f1f1;
  --dark:#1c1c1c;
  --darker:#111;
}
*{box-sizing:border-box;margin:0;padding:0}
html,body{width:690px;height:1200px;overflow:hidden}
body{background:var(--darker);font-family:"Open Sans",Arial,sans-serif;color:var(--text);font-size:7px;line-height:1.5}
main{background:var(--paper)}
.wrap{width:500px;margin:0 auto;position:relative}

/* header */
.site-header{height:66px;background:var(--paper);border-bottom:1px solid var(--line)}
.site-header .wrap{height:66px}
.brand{position:absolute;left:0;top:14px;display:flex;align-items:center;gap:7px}
.brand-dot{width:28px;height:28px;border-radius:50%;background:#555}
.brand-name{font-weight:700;font-size:11px;line-height:1.15;color:var(--ink);text-transform:uppercase;width:120px}
.util-links{position:absolute;right:0;top:8px;display:flex;gap:12px;font-size:6px;color:var(--muted)}
.main-nav{position:absolute;right:0;top:28px;display:flex;gap:2px}
.main-nav a{display:block;padding:5px 9px;font-size:7px;font-weight:600;text-transform:uppercase;color:var(--ink);text-decoration:none;border:1px solid transparent}
.main-nav a.active{border-color:var(--orange);color:var(--orange)}

/* hero */
.hero{height:209px;position:relative;overflow:hidden;background:linear-gradient(180deg,#d9d9d9 0%,#eaeaea 55%,#f6f6f6 100%)}
.hero-skyline{position:absolute;inset:0;background:linear-gradient(90deg,#c9c9c9 0%,#dedede 45%,#e9e9e9 100%);opacity:.9}
.hero-people{position:absolute;right:95px;bottom:0;width:260px;height:200px;background:linear-gradient(160deg,#d6b48c 0%,#e5c76a 35%,#8fa3b8 70%,#5f6f80 100%);border-radius:120px 120px 0 0;opacity:.85}
.hero-copy{position:absolute;left:95px;top:46px}
.hero-kicker{font-weight:700;font-size:12px;letter-spacing:2px;color:var(--paper);text-transform:uppercase;line-height:1.25;width:170px}
.hero-bar{width:130px;height:3px;background:var(--orange);margin:7px 0 6px}
.hero-title{font-weight:800;font-size:36px;line-height:1;color:var(--ink);text-transform:uppercase}

/* welcome */
.welcome{padding-top:12px}
.welcome .wrap{display:flex;align-items:center;border:1px solid var(--line);height:48px;padding:0 14px}
.welcome h1{flex:none;font-family:"Oswald",sans-serif;font-weight:400;font-size:24px;color:var(--orange);padding-right:14px;border-right:1px solid var(--line);line-height:34px}
.welcome p{padding-left:14px;font-size:7px;color:var(--text)}

/* section title */
.section-title{display:flex;align-items:center;justify-content:center;gap:10px;font-weight:600;font-size:11px;color:var(--orange);text-transform:uppercase;letter-spacing:.5px;line-height:16px}
.section-title::before,.section-title::after{content:"";width:150px;height:1px;background:var(--line)}

/* services */
.services{padding:16px 0 24px}
.services-intro{text-align:center;font-size:6.3px;margin:7px auto 12px;width:480px;color:var(--text)}
.service-grid{display:grid;grid-template-columns:repeat(3,1fr);gap:12px 14px}
.service-card{height:96px;border:1px solid var(--line);padding:7px;position:relative;background:var(--paper)}
.service-card.featured{background:#151515;border-color:#151515}
.service-card h3{font-size:7.5px;font-weight:700;color:var(--orange);text-transform:uppercase;line-height:1.25;width:62px}
.service-card.featured h3{color:var(--paper)}
.service-media{position:absolute;right:7px;top:7px;width:80px;height:46px}
.service-card p{position:absolute;left:7px;top:56px;width:72px;font-size:5.5px;line-height:1.45;color:var(--muted)}
.service-card.featured p{color:#aaa}
.learn-more{position:absolute;right:7px;bottom:7px;background:#555;color:var(--paper);font-size:5.5px;font-weight:600;padding:3px 7px;text-transform:uppercase}
.service-card.featured .learn-more{background:var(--orange)}

/* news */
.news{height:150px}
.news-grid{display:grid;grid-template-columns:1fr 1fr;gap:30px;margin-top:16px}
.news-item{display:grid;grid-template-columns:38px 1fr;column-gap:8px}
.news-date{font-family:"Oswald",sans-serif;color:var(--orange)}
.news-date b{display:block;font-weight:400;font-size:26px;line-height:1}
.news-date span{display:block;font-size:8px;color:var(--ink);letter-spacing:1px}
.news-item h4{font-size:8px;font-weight:700;color:var(--orange);line-height:1.3}
.news-item p{font-size:6px;margin-top:4px}
.read-more{grid-column:1/3;justify-self:start;margin-top:10px;border:1px solid #bbb;padding:3px 9px;font-size:6px;color:var(--ink)}

/* clients */
.clients{background:var(--soft);height:122px;padding-top:12px}
.clients .section-title::before,.clients .section-title::after{background:#d8d8d8}
.testimonial{position:relative;width:410px;margin:8px auto 0;text-align:center}
.testimonial blockquote{font-style:italic;font-size:6.5px;color:var(--text);padding:0 30px}
.quote-mark{position:absolute;top:-8px;font-family:Georgia,serif;font-size:42px;line-height:1;color:var(--orange)}
.quote-mark.open{left:0}
.quote-mark.close{right:0;top:12px}
.client{display:flex;align-items:center;justify-content:center;gap:7px;margin-top:8px}
.client-photo{width:28px;height:28px;border-radius:50%;background:linear-gradient(135deg,#8a6a55,#c7a58a)}
.client-name{font-size:6.5px;font-weight:700;color:var(--orange);text-transform:uppercase}

/* contact */
.contact{height:240px;background:linear-gradient(180deg,#2a2a2a 0%,var(--dark) 40%,#191919 100%);padding-top:20px}
.contact-title{text-align:center;color:var(--paper);font-weight:600;font-size:14px;letter-spacing:1.5px;text-transform:uppercase}
.contact-title::after{content:"";display:block;width:40px;height:2px;background:var(--orange);margin:6px auto 0}
.contact-body{display:grid;grid-template-columns:190px 1fr;gap:24px;margin-top:20px}
.contact-list{list-style:none}
.contact-list li{display:flex;gap:7px;align-items:flex-start;font-size:6.5px;color:#bbb;margin-bottom:11px}
.contact-list svg{flex:none;width:10px;height:10px}
.social{display:flex;gap:10px;margin-top:22px}
.social span{width:16px;height:16px;border-radius:50%;background:#3a3a3a}
.social span:first-child{background:var(--orange)}
.contact-form{display:grid;grid-template-columns:1fr 1fr;gap:8px}
.field{border:1px solid #3d3d3d;background:#202020;height:22px;padding:6px 8px;font-size:6.5px;color:#888}
.field.message{grid-column:1/3;height:64px}
.send{grid-column:1/3;justify-self:end;width:144px;height:22px;background:var(--orange);color:var(--paper);font-weight:700;font-size:7px;letter-spacing:1.5px;text-transform:uppercase;text-align:center;line-height:22px}

/* footer */
.site-footer{height:56px;background:var(--darker);text-align:center;padding-top:12px;font-size:5.8px;color:#777}
</style>
</head>
<body>
<main>
<header class="site-header">
  <div class="wrap">
    <div class="brand">
      <span class="brand-dot"></span>
      <span class="brand-name">Brackwell Counsel Partners</span>
    </div>
    <div class="util-links"><span>Client Login</span><span>Terms &amp; Conditions</span><span>Sitemap</span></div>
    <nav class="main-nav">
      <a class="active" href="#">Home</a>
      <a href="#">About Us</a>
      <a href="#">Join Us</a>
      <a href="#">News</a>
      <a href="#">Contact</a>
      <a href="#">Blog</a>
    </nav>
  </div>
</header>

<section class="hero">
  <div class="hero-skyline" role="img" aria-label="Soft grey city skyline in the background"></div>
  <div class="hero-people" role="img" aria-label="Group of smiling students holding books and backpacks"></div>
  <div class="hero-copy">
    <div class="hero-kicker">Brackwell Counsel Partners</div>
    <div class="hero-bar"></div>
    <div class="hero-title">Student<br>Visa</div>
  </div>
</section>

<section class="welcome">
  <div class="wrap">
    <h1>WELCOME!</h1>
    <p>We are Immigration Lawyers regulated by the Immigration Advice Standards Board at the highest level (Level 3) and accredited by the Northgate Legal Guild in England and Wales.</p>
  </div>
</section>

<section class="services">
  <div class="wrap">
    <h2 class="section-title">Our Services</h2>
    <p class="services-intro">We provide expert advice on every stage of your UK immigration journey, from first enquiry to final decision. Our experienced team handles work, family, study and business applications with care, clear fixed fees and a friendly, professional approach you can trust.</p>
    <div class="service-grid">
      <article class="service-card featured">
        <h3>Work<br>Visas</h3>
        <div class="service-media" role="img" aria-label="Professionals at work in an office" style="background:linear-gradient(135deg,#6b6b6b,#a8a8a8)"></div>
        <p>Skilled worker and sponsor licence support for employers.</p>
        <span class="learn-more">Learn more</span>
      </article>
      <article class="service-card">
        <h3>Visitor<br>Visas</h3>
        <div class="service-media" role="img" aria-label="Visitors travelling with luggage" style="background:linear-gradient(135deg,#8aa0b5,#c9d3dc)"></div>
        <p>Tourist and family visit applications made simple.</p>
        <span class="learn-more">Learn more</span>
      </article>
      <article class="service-card">
        <h3>Working<br>Holiday Visa</h3>
        <div class="service-media" role="img" aria-label="Young worker on a working holiday" style="background:linear-gradient(135deg,#3f6fa8,#9bb7d6)"></div>
        <p>Youth mobility schemes for young people abroad.</p>
        <span class="learn-more">Learn more</span>
      </article>
      <article class="service-card">
        <h3>Family<br>Visas</h3>
        <div class="service-media" role="img" aria-label="Family together at home" style="background:linear-gradient(135deg,#c89a7a,#e6cdb8)"></div>
        <p>Spouse, partner and child visas to reunite families.</p>
        <span class="learn-more">Learn more</span>
      </article>
      <article class="service-card">
        <h3>Study<br>Visas</h3>
        <div class="service-media" role="img" aria-label="Students studying together" style="background:linear-gradient(135deg,#9a8a78,#d8cbbd)"></div>
        <p>Student routes for universities and colleges.</p>
        <span class="learn-more">Learn more</span>
      </article>
      <article class="service-card">
        <h3>Business<br>Visas</h3>
        <div class="service-media" role="img" aria-label="Business people in a meeting" style="background:linear-gradient(135deg,#6e7d8c,#b9c3cc)"></div>
        <p>Investor and innovator routes for entrepreneurs.</p>
        <span class="learn-more">Learn more</span>
      </article>
    </div>
  </div>
</section>

<section class="news">
  <div class="wrap">
    <h2 class="section-title">Latest News</h2>
    <div class="news-grid">
      <article class="news-item">
        <div class="news-date"><b>11</b><span>JUNE</span></div>
        <div>
          <h4>Lorem ipsum dolor sit amet consectetur elit.</h4>
          <p>Lorem ipsum dolor sit amet, consectetur adipiscing elit. Nunc vel libero in est aliquet gravida. Sed ac tincidunt nisl, sed vulputate mi.</p>
        </div>
        <span class="read-more">Read More</span>
      </article>
      <article class="news-item">
        <div class="news-date"><b>15</b><span>JUNE</span></div>
        <div>
          <h4>Lorem ipsum dolor sit amet consectetur elit.</h4>
          <p>Lorem ipsum dolor sit amet, consectetur adipiscing elit. Nunc vel libero in est aliquet gravida. Sed ac tincidunt nisl, sed vulputate mi.</p>
        </div>
        <span class="read-more">Read More</span>
      </article>
    </div>
  </div>
</section>

<section class="clients">
  <div class="wrap">
    <h2 class="section-title">Happy Clients</h2>
    <div class="testimonial">
      <span class="quote-mark open">&ldquo;</span>
      <blockquote>The team guided me through my student visa from start to finish. Every question was answered quickly and the fees were clear from the first meeting. I felt supported at every step and my application was approved without delay. I would happily recommend them to anyone.</blockquote>
      <span class="quote-mark close">&rdquo;</span>
      <div class="client">
        <span class="client-photo" role="img" aria-label="Portrait of the client"></span>
        <span class="client-name">Amelia Hartwell</span>
      </div>
    </div>
  </div>
</section>

<section class="contact">
  <div class="wrap">
    <h2 class="contact-title">Get in Touch</h2>
    <div class="contact-body">
      <div>
        <ul class="contact-list">
          <li>
            <svg viewBox="0 0 10 10"><path d="M5 .5a3.2 3.2 0 0 0-3.2 3.2C1.8 6 5 9.5 5 9.5S8.2 6 8.2 3.7A3.2 3.2 0 0 0 5 .5z" fill="#f26b21"/><circle cx="5" cy="3.7" r="1.2" fill="#1c1c1c"/></svg>
            <span>London Office, Brackwell Counsel Partners,<br>24 Carrow Lane, London EC2A 9QT</span>
          </li>
          <li>
            <svg viewBox="0 0 10 10"><path d="M2.2 .8l1.6 1.9-.9 1.2a6 6 0 0 0 3.2 3.2l1.2-.9 1.9 1.6-.9 1.4C5 9 1 5 .8 1.7z" fill="#f26b21"/></svg>
            <span>0207 555 0142</span>
          </li>
          <li>
            <svg viewBox="0 0 10 10"><rect x=".5" y="2" width="9" height="6.2" fill="none" stroke="#f26b21"/><path d="M.5 2L5 5.6 9.5 2" fill="none" stroke="#f26b21"/></svg>
            <span>hello@brackwellcounsel.co.uk</span>
          </li>
        </ul>
        <div class="social"><span></span><span></span><span></span><span></span></div>
      </div>
      <div class="contact-form">
        <div class="field">Your Name</div>
        <div class="field">Your Email</div>
        <div class="field message">Message</div>
        <div class="send">Send Message</div>
      </div>
    </div>
  </div>
</section>

<footer class="site-footer">
  Regulated by the Immigration Advice Standards Board. Registered in England and Wales.<br>
  &copy; Brackwell Counsel Partners. All Rights Reserved.
</footer>
</main>
</body>
</html>
```